New Brochure Design Project

I would like to purchase a customized version of a design you have previously submitted - https://www.pixelbazaar.example/design/52910476

We Are a Freight Brokerage company based out of Pennsylvania. Company name is Harborline Cargo Partners. Phone number 555-283-9104. Email is harborlinecargopartners@mailvista.example please design it with trucks like the front page of this brochure example template or New trucks from USA preferably Roadmarshals Tundrax.

Target Market(s)

Shippers

Industry/Entity Type

Logistics

Requirements
Must have
• must be a brochure not a simple front and back flyer.

Also we would like bulletins to describe what our business offers and what we are geared towards. something that is not to informative that it bores them but something that is eye catching that will attract the person it is meant for to want to take a look at it.
Bulletin Ideas:
WHAT WE DO
“ What sets Harborline Cargo Partners apart from other transportation providers? Our mission
is to bring value to customers by gaining an understanding of their business and then delivering customized shipping solutions.
With 30-plus years in asset-based and third-party transportation management, we know how to make it happen.”
*OURROUTESDELIVER
Looking to control transportation-related costs and find cost-effective alternatives? Harborline Cargo Partners provides the transportation know-how to help you create a unique competitive edge - each and every day.
Turn to Harborline Cargo Partners and you’ll get:

• Access to freight capacity
• Powerful technology that provides visibility into shipment status and details
• Staff accessibility, including communication routed directly to their mobile devices during non-business hours
• Best-in-breed technology platforms for optimum efficiencies and reporting in brokerage, fleet and transportation management, freight bill audit and payment.
TECHNOLOGY AND VISIBILITY
Power your supply chain by Harborline Cargo Partners RouteDesk Suite, giving you access to best-in-breed systems, capabilities, and reporting to manage your entire transportation processes.
• Supply chain visibility from order entry and dispatch through logistics management and settlement
• Accurate, comprehensive visibility to shipping costs and activities
• Shipment routing, tracking, rating, pricing, and delivery measurement
Performance
SUPPLY CHAIN SOLUTIONS
Our culture at Harborline Cargo Partners encourages delivery of high performance in service as well as your shipments.
• Each team member has solid transportation expertise
• Close relationships with our carrier partners and drivers delivering your freight
• Resourceful, accountable, accessible
• Able to make immediate decisions, solve complex problems
• Backed by 10 years in business
OUR FEATURES INCLUDE:
Time saving order management features
Load auto-posting to over 43 leading load boards
Real time FMCSA carrier safety / authority data
Automated carrier due diligence
Smart search truck matching
E-update program emails Shippers with status changes
Flexible invoicing options
Detailed reporting and analytics
Online tracking / order visibility
Key performance metrics dashboard for carrier performance

Address: 942 Oberly Ln, Wrenford Vale 00000

```html
<!DOCTYPE html>
<html lang="en">
<head>
<meta charset="utf-8">
<title>Harborline Cargo Partners – Trifold Brochure</title>
<link rel="stylesheet" href="https://fonts.googleapis.com/css2?family=Montserrat:wght@400;600;700;800;900&family=Open+Sans:wght@400;600&display=swap">
<style>
:root{
  --red:#d3202a;
  --ink:#2a2a2c;
  --text:#4a4a4e;
  --muted:#8a8a90;
  --paper:#ffffff;
  --stage:#e4e4e6;
  --photo-sky:#8fb3d4;
  --photo-steel:#7d848c;
  --photo-warm:#c9a88a;
}
*{box-sizing:border-box;margin:0;padding:0}
html,body{width:1200px;height:2396px;overflow:hidden}
body{background:var(--stage);font-family:"Open Sans",Arial,sans-serif;color:var(--text);position:relative}
.spread{position:absolute;left:40px;width:1120px;height:866px;display:grid;grid-template-columns:repeat(3,1fr);background:var(--paper);box-shadow:0 10px 30px rgba(0,0,0,.18)}
.spread--outside{top:250px}
.spread--inside{top:1290px}
.panel{position:relative;overflow:hidden;padding:40px 32px 90px}
.panel + .panel{border-left:1px solid #ececee}
.heading{font-family:"Montserrat",Arial,sans-serif;font-weight:800;color:var(--red);font-size:20px;line-height:1.2;letter-spacing:.5px;text-transform:uppercase;margin-bottom:12px}
.body-copy{font-size:12.5px;line-height:1.6;margin-bottom:12px}
.bullets{list-style:none;font-size:12px;line-height:1.5}
.bullets li{position:relative;padding-left:18px;margin-bottom:7px}
.bullets li::before{content:"";position:absolute;left:2px;top:6px;width:7px;height:7px;background:var(--red);border-radius:50%}
.checks{list-style:none;font-size:12px;line-height:1.45}
.checks li{display:flex;gap:9px;align-items:flex-start;margin-bottom:8px}
.checks svg{flex:none;margin-top:2px}
.photo{display:block}
.brand{display:flex;align-items:center;gap:10px;font-family:"Montserrat",Arial,sans-serif;font-weight:800;color:var(--red);font-size:19px;line-height:1.15;text-transform:uppercase}
.brand__mark{width:22px;height:22px;background:var(--red);flex:none}
.band{position:absolute;left:0;right:0;bottom:0;width:100%;height:70px}
.contact{list-style:none;font-size:12px;line-height:1.4}
.contact li{display:flex;gap:10px;align-items:center;margin-bottom:10px;overflow-wrap:anywhere}
.contact svg{flex:none}
.web{position:absolute;left:32px;bottom:22px;font-family:"Montserrat",Arial,sans-serif;font-weight:600;font-size:11.5px;color:#fff;z-index:2}
.cover{padding:0}
.cover .brand{position:absolute;top:42px;left:34px;right:30px}
.cover__photo{position:absolute;top:150px;left:0;width:100%;height:420px}
.cover__headline{position:absolute;left:40px;top:600px;font-family:"Montserrat",Arial,sans-serif;font-weight:900;font-size:64px;line-height:1;color:var(--ink);letter-spacing:2px}
.cover__tag{position:absolute;left:0;right:0;top:700px;height:54px;background:var(--red);color:#fff;font-family:"Montserrat",Arial,sans-serif;font-weight:700;font-size:15px;letter-spacing:1.5px;display:flex;align-items:center;padding-left:40px}
.cover__sub{position:absolute;left:40px;top:772px;font-size:13px;color:var(--muted);font-weight:600}
.circle-photo{border-radius:50%;border:6px solid var(--red);overflow:hidden;display:block}
.center{text-align:center}
</style>
</head>
<body>

<section class="spread spread--outside">
  <article class="panel">
    <h2 class="heading">What We Do</h2>
    <p class="body-copy">What sets Harborline Cargo Partners apart from other transportation providers? Our mission is to bring value to customers by gaining an understanding of their business and then delivering customized shipping solutions.</p>
    <p class="body-copy">With 30-plus years in asset-based and third-party transportation management, we know how to make it happen.</p>
    <svg class="photo" role="img" aria-label="Photo of a modern semi truck on the highway" width="309" height="260" viewBox="0 0 309 260" style="margin:14px 0 18px">
      <defs><linearGradient id="g1" x1="0" y1="0" x2="1" y2="1"><stop offset="0" stop-color="#b9c7d4"/><stop offset="1" stop-color="#5d646c"/></linearGradient></defs>
      <path d="M0 0H309V200Q160 270 0 220Z" fill="url(#g1)"/>
      <path d="M0 220Q160 270 309 200V214Q160 284 0 234Z" fill="var(--red)"/>
    </svg>
    <ul class="contact">
      <li><svg width="16" height="16" viewBox="0 0 16 16"><path d="M8 1a5 5 0 0 0-5 5c0 4 5 9 5 9s5-5 5-9a5 5 0 0 0-5-5zm0 7a2 2 0 1 1 0-4 2 2 0 0 1 0 4z" fill="var(--red)"/></svg>942 Oberly Ln, Wrenford Vale 00000</li>
    </ul>
    <svg class="band" viewBox="0 0 373 70" preserveAspectRatio="none"><path d="M0 30Q190 -10 373 20V70H0Z" fill="var(--red)"/></svg>
  </article>

  <article class="panel center">
    <svg class="circle-photo" role="img" aria-label="Photo of a warehouse worker handling boxed freight" width="210" height="210" viewBox="0 0 210 210" style="margin:10px auto 26px">
      <defs><linearGradient id="g2" x1="0" y1="0" x2="1" y2="1"><stop offset="0" stop-color="#e3d2bf"/><stop offset="1" stop-color="var(--photo-warm)"/></linearGradient></defs>
      <rect width="210" height="210" fill="url(#g2)"/>
    </svg>
    <div class="brand" style="justify-content:center;margin-bottom:20px"><span class="brand__mark"></span><span>Harborline Cargo<br>Partners</span></div>
    <p class="body-copy">Freight brokerage for shippers who need capacity, visibility and people who answer the phone.</p>
    <svg class="photo" role="img" aria-label="Photo of a tractor trailer at a loading dock" width="309" height="170" viewBox="0 0 309 170" style="margin:18px 0 20px">
      <defs><linearGradient id="g3" x1="0" y1="0" x2="1" y2="0"><stop offset="0" stop-color="#9aa3ac"/><stop offset="1" stop-color="#3f454b"/></linearGradient></defs>
      <rect width="309" height="170" rx="10" fill="url(#g3)"/>
    </svg>
    <ul class="contact" style="text-align:left">
      <li><svg width="16" height="16" viewBox="0 0 16 16"><path d="M4 1l3 3-2 2c1 2 3 4 5 5l2-2 3 3-2 2C7 14 2 9 1 3z" fill="var(--red)"/></svg>555-283-9104</li>
      <li><svg width="16" height="16" viewBox="0 0 16 16"><rect x="1" y="3" width="14" height="10" rx="1" fill="var(--red)"/><path d="M1 4l7 5 7-5" stroke="#fff" fill="none"/></svg>harborlinecargopartners@mailvista.example</li>
    </ul>
  </article>

  <article class="panel cover">
    <div class="brand"><span class="brand__mark"></span><span>Harborline Cargo<br>Partners</span></div>
    <svg class="cover__photo" role="img" aria-label="Photo of a Roadmarshals Tundrax semi truck against a blue sky" viewBox="0 0 373 420" preserveAspectRatio="none">
      <defs><linearGradient id="g4" x1="0" y1="0" x2="0" y2="1"><stop offset="0" stop-color="var(--photo-sky)"/><stop offset=".6" stop-color="#c9d3dc"/><stop offset="1" stop-color="var(--photo-steel)"/></linearGradient></defs>
      <path d="M0 20Q190 -10 373 10V360Q180 430 0 380Z" fill="url(#g4)"/>
      <path d="M0 380Q180 430 373 360V384Q180 454 0 404Z" fill="var(--red)"/>
    </svg>
    <div class="cover__headline">FAST</div>
    <div class="cover__tag">RELIABLE FREIGHT BROKERAGE</div>
    <div class="cover__sub">Shipping solutions built around you</div>
    <svg class="band" viewBox="0 0 373 70" preserveAspectRatio="none"><path d="M0 40Q200 0 373 30V70H0Z" fill="var(--red)"/></svg>
  </article>
</section>

<section class="spread spread--inside">
  <article class="panel">
    <h2 class="heading">*OurRoutesDeliver</h2>
    <p class="body-copy">Looking to control transportation-related costs and find cost-effective alternatives? Harborline Cargo Partners provides the transportation know-how to help you create a unique competitive edge - each and every day.</p>
    <p class="body-copy" style="font-weight:600;color:var(--ink)">Turn to Harborline Cargo Partners and you’ll get:</p>
    <ul class="bullets">
      <li>Access to freight capacity</li>
      <li>Powerful technology that provides visibility into shipment status and details</li>
      <li>Staff accessibility, including communication routed directly to their mobile devices during non-business hours</li>
      <li>Best-in-breed technology platforms for optimum efficiencies and reporting in brokerage, fleet and transportation management, freight bill audit and payment.</li>
    </ul>
    <svg class="photo" role="img" aria-label="Photo of a white semi truck on the road" width="309" height="170" viewBox="0 0 309 170" style="margin-top:16px">
      <defs><linearGradient id="g5" x1="0" y1="0" x2="1" y2="1"><stop offset="0" stop-color="#c8d2da"/><stop offset="1" stop-color="#6d747b"/></linearGradient></defs>
      <rect width="309" height="170" rx="10" fill="url(#g5)"/>
    </svg>
    <svg class="band" viewBox="0 0 373 70" preserveAspectRatio="none"><path d="M0 30Q190 -5 373 22V70H0Z" fill="var(--red)"/></svg>
    <div class="web">www.harborlinecargopartners.example</div>
  </article>

  <article class="panel">
    <svg class="circle-photo" role="img" aria-label="Photo of a dispatcher tracking shipments on screens" width="170" height="170" viewBox="0 0 170 170" style="margin:0 auto 18px">
      <defs><linearGradient id="g6" x1="0" y1="0" x2="1" y2="1"><stop offset="0" stop-color="#d9c3ab"/><stop offset="1" stop-color="#8a6f57"/></linearGradient></defs>
      <rect width="170" height="170" fill="url(#g6)"/>
    </svg>
    <h2 class="heading">Technology and Visibility</h2>
    <p class="body-copy">Power your supply chain by Harborline Cargo Partners RouteDesk Suite, giving you access to best-in-breed systems, capabilities, and reporting to manage your entire transportation processes.</p>
    <ul class="bullets">
      <li>Supply chain visibility from order entry and dispatch through logistics management and settlement</li>
      <li>Accurate, comprehensive visibility to shipping costs and activities</li>
      <li>Shipment routing, tracking, rating, pricing, and delivery measurement</li>
    </ul>
    <h2 class="heading" style="margin-top:16px">Supply Chain Solutions</h2>
    <ul class="bullets">
      <li>Each team member has solid transportation expertise</li>
      <li>Close relationships with our carrier partners and drivers delivering your freight</li>
      <li>Resourceful, accountable, accessible</li>
      <li>Able to make immediate decisions, solve complex problems</li>
      <li>Backed by 10 years in business</li>
    </ul>
  </article>

  <article class="panel">
    <svg class="photo" role="img" aria-label="Photo of a semi truck fleet parked at sunset" width="309" height="200" viewBox="0 0 309 200" style="margin-bottom:22px">
      <defs><linearGradient id="g7" x1="0" y1="0" x2="0" y2="1"><stop offset="0" stop-color="#e0a97a"/><stop offset="1" stop-color="#4d4f57"/></linearGradient></defs>
      <rect width="309" height="200" rx="12" fill="url(#g7)"/>
    </svg>
    <h2 class="heading">Our Features Include:</h2>
    <ul class="checks">
      <li><svg width="14" height="14" viewBox="0 0 14 14"><circle cx="7" cy="7" r="7" fill="var(--red)"/><path d="M4 7l2 2 4-4" stroke="#fff" stroke-width="1.6" fill="none"/></svg>Time saving order management features</li>
      <li><svg width="14" height="14" viewBox="0 0 14 14"><circle cx="7" cy="7" r="7" fill="var(--red)"/><path d="M4 7l2 2 4-4" stroke="#fff" stroke-width="1.6" fill="none"/></svg>Load auto-posting to over 43 leading load boards</li>
      <li><svg width="14" height="14" viewBox="0 0 14 14"><circle cx="7" cy="7" r="7" fill="var(--red)"/><path d="M4 7l2 2 4-4" stroke="#fff" stroke-width="1.6" fill="none"/></svg>Real time FMCSA carrier safety / authority data</li>
      <li><svg width="14" height="14" viewBox="0 0 14 14"><circle cx="7" cy="7" r="7" fill="var(--red)"/><path d="M4 7l2 2 4-4" stroke="#fff" stroke-width="1.6" fill="none"/></svg>Automated carrier due diligence</li>
      <li><svg width="14" height="14" viewBox="0 0 14 14"><circle cx="7" cy="7" r="7" fill="var(--red)"/><path d="M4 7l2 2 4-4" stroke="#fff" stroke-width="1.6" fill="none"/></svg>Smart search truck matching</li>
      <li><svg width="14" height="14" viewBox="0 0 14 14"><circle cx="7" cy="7" r="7" fill="var(--red)"/><path d="M4 7l2 2 4-4" stroke="#fff" stroke-width="1.6" fill="none"/></svg>E-update program emails Shippers with status changes</li>
      <li><svg width="14" height="14" viewBox="0 0 14 14"><circle cx="7" cy="7" r="7" fill="var(--red)"/><path d="M4 7l2 2 4-4" stroke="#fff" stroke-width="1.6" fill="none"/></svg>Flexible invoicing options</li>
      <li><svg width="14" height="14" viewBox="0 0 14 14"><circle cx="7" cy="7" r="7" fill="var(--red)"/><path d="M4 7l2 2 4-4" stroke="#fff" stroke-width="1.6" fill="none"/></svg>Detailed reporting and analytics</li>
      <li><svg width="14" height="14" viewBox="0 0 14 14"><circle cx="7" cy="7" r="7" fill="var(--red)"/><path d="M4 7l2 2 4-4" stroke="#fff" stroke-width="1.6" fill="none"/></svg>Online tracking / order visibility</li>
      <li><svg width="14" height="14" viewBox="0 0 14 14"><circle cx="7" cy="7" r="7" fill="var(--red)"/><path d="M4 7l2 2 4-4" stroke="#fff" stroke-width="1.6" fill="none"/></svg>Key performance metrics dashboard for carrier performance</li>
    </ul>
    <svg class="band" viewBox="0 0 373 70" preserveAspectRatio="none"><path d="M0 22Q180 -5 373 32V70H0Z" fill="var(--red)"/></svg>
  </article>
</section>

</body>
</html>
```